Cobalt Landscaping Landing Page

I require a landing page for my landscaping business.

My business plan revolves around hooking clients with weeding services. Not lawn herbicide sprays, but actual hand weeding and bed maintenance. I've found my niche as most people do not want to do this kind of work. From there I often upsell clients into actual hardscaping or softscaping.

I like things to be clean, concise, and to the point. Not overly flashy, but not so minimal that that it's boring. My logo is a very good example of what I like.

The business is LGBTQ owned and operated. I do not broadcast this but I feel the logo itself, along with the name is usually enough to tip people into assumption. I'm not opposed to color, but I do not want the page to scream "gay". My favourite color is yellow...

I used to be a door to door salesman so I'm doing something different where I want to do all my selling in my first meeting with the client. With this said I do not need a section for "work pictures", as I have photos of my work on my tablet, which I show the client during the consultation.

Ideally i'd like my web site to actually be just a landing page. I'd like room for all the following information within the page;

- description of services;
Weeding of Perennial and Flower Beds
Selective Pruning of Trees and Shrubs
Hedging
Landscape Construction
Landscape Design
Total Lawn Treatment Plans
Landscape Pest Control

- contact information, phone, email
Gerald Ostrunek
204-571-3342
ger.ostrunek@maplethorn.com

- "free estimates" somewhere on the page that is either led to by the eye, or very easy to notice and see

- and my slogan which is "dependable, reliable, consistent"

- room for a link to my future revuly account so they can see reviews from real people

- My Logo present

Any or all of these can be custom made graphics or simply text, whatever looks best

I do not want people to have to search for information throughout. Design it in such a way that either the eye flows naturally from one piece of information to the other, or that it's all compartmentalized neatly enough that everything is easy to find.

As I am a landscape and outdoor maintenance service I'm no opposed to images such as flowers, trees, landscaping, etc being present. However please note that my main focus and source of income comes from weeding services, everything else is bonus cash.

Many of my clients are extremely wealthy individuals who pay over $1000 for the season for me just to show up and pull weeds. So making the website appeal to wealthy people as opposed to the average joe is paramount.

I do not cut grass. Please do not have any indication on the website, either through writing or graphics that implies that I cut grass. There are enough companies doing that.

Target Market(s)

Wealthy, often elderly individuals.

Industry/Entity Type

Landscape Gardening

Coding

Coded - Design and coding required

Number of Pages Required

1 page

Font styles to use
Sans Serif

Colors

Designer to choose colors to be used in the design.

Requirements
Must have
• - description of services;
• Weeding of Perennial and Flower Beds
• Selective Pruning of Trees and Shrubs
• Hedging
• Landscape Construction
• Landscape Design
• Total Lawn Treatment Plans
• Landscape Pest Control
• - contact information, phone, email
• Gerald Ostrunek
• 204-571-3342
• ger.ostrunek@maplethorn.com
• - "free estimates" somewhere on the page that is either led to by the eye, or very easy to notice and see
• - and my slogan which is "dependable, reliable, consistent"
• - room for a link to my future revuly account so they can see reviews from real people
• - My Logo present
Nice to have
• Flowers or weeds depicted. Possibly some hardscaping and softscaping if it doesnt look too bulky and crowded.
Should not have
• grass

```html
<!DOCTYPE html>
<html lang="en">
<head>
<meta charset="utf-8">
<title>Cobalt Landscaping</title>
<link href="https://fonts.googleapis.com/css2?family=Questrial&family=Montserrat:wght@400;600;700&display=swap" rel="stylesheet">
<style>
:root{
  --green:#5c9a1b;
  --green-dark:#3f7410;
  --orange:#f26a21;
  --ink:#2a2a2a;
  --muted:#7a7a7a;
  --light:#f2f2f2;
  --footer:#1f1f1d;
  --purple:#5b2a86;
  --red:#d7262b;
  --yellow:#f4c400;
  --blue:#2b5aa8;
  --slogan:#cfe06a;
}
*{box-sizing:border-box;margin:0;padding:0}
html,body{width:1200px;height:5172px;overflow:hidden}
body{font-family:"Questrial",sans-serif;color:var(--ink);background:#fff;position:relative}
.section{position:absolute;left:0;width:1200px}
.heading{font-family:"Montserrat",sans-serif;font-size:28px;font-weight:400;letter-spacing:1px;text-transform:uppercase;color:var(--ink)}
.heading b{font-weight:700}
.divider{display:flex;align-items:center;gap:8px;height:14px}
.divider span{display:block;width:36px;height:1px;background:#bbb}
.divider i{display:block;width:12px;height:12px;border-radius:50%;background:var(--yellow)}
.center{text-align:center}
.center .divider{justify-content:center}

/* top bar */
.topbar{top:0;height:41px;background:#fff;font-size:12px;color:var(--muted)}
.topbar .contact{position:absolute;left:80px;top:0;height:41px;display:flex;align-items:center;gap:30px}
.topbar .contact span{display:flex;align-items:center;gap:7px}
.estimate-tab{position:absolute;left:793px;top:0;width:155px;height:41px;background:var(--orange);color:#fff;font-family:"Montserrat",sans-serif;font-weight:700;font-size:12px;display:flex;align-items:center;justify-content:center;letter-spacing:.5px}
.social{position:absolute;display:flex;gap:12px}
.topbar .social{left:968px;top:7px}
.social i{display:block;width:27px;height:27px;border-radius:50%;background:var(--green)}

/* nav */
.nav{top:41px;height:104px;background:#fff;border-top:1px solid #eee}
.logo{position:absolute;display:flex;align-items:center;gap:10px;font-family:"Montserrat",sans-serif;font-weight:700;font-size:25px;letter-spacing:.5px;color:var(--ink)}
.logo i{display:block;width:18px;height:18px;border-radius:50%;background:var(--yellow)}
.nav .logo{left:80px;top:36px}
.menu{position:absolute;right:80px;top:44px;display:flex;gap:26px;font-size:13px;font-weight:600;font-family:"Montserrat",sans-serif;color:#444}

/* hero */
.hero{top:145px;height:641px;background:linear-gradient(180deg,#e9e6d7 0%,#c4cf9a 35%,#6a9b2c 70%,#4f8a1e 100%)}
.slogan{position:absolute;left:0;width:1200px;text-align:center;font-family:"Montserrat",sans-serif;font-weight:700;font-size:50px;letter-spacing:3px;color:var(--slogan)}
.slogan span{display:inline-block;background:rgba(0,0,0,.72);padding:4px 18px}
.slogan.one{top:246px}
.slogan.two{top:328px}

/* about */
.about{top:786px;height:576px;background:#fff}
.about .heading{position:absolute;top:64px;width:100%}
.about .divider{position:absolute;top:124px;width:100%}
.about .lead{position:absolute;top:168px;left:290px;width:620px;font-size:14px;line-height:24px;color:var(--muted)}
.features{position:absolute;top:317px;left:80px;display:flex;gap:25px}
.feature{width:241px;height:180px;background:#f5f5f5;border-bottom:4px solid;text-align:center;font-family:"Montserrat",sans-serif;font-size:12px;font-weight:700;text-transform:uppercase}
.feature .badge{width:46px;height:46px;border-radius:50%;margin:38px auto 0;display:flex;align-items:center;justify-content:center}
.feature .label{margin-top:40px;line-height:16px;color:var(--ink)}
.f-purple{border-color:var(--purple)}.f-purple .badge{background:var(--purple)}
.f-red{border-color:var(--red)}.f-red .badge{background:var(--red)}
.f-yellow{border-color:var(--yellow)}.f-yellow .badge{background:var(--yellow)}
.f-blue{border-color:var(--blue)}.f-blue .badge{background:var(--blue)}

/* services */
.services{top:1362px;height:1207px;background:linear-gradient(160deg,#26321d 0%,#1c2a16 40%,#3c5a22 75%,#2a3d1a 100%)}
.services .heading{position:absolute;top:76px;width:100%;color:#fff}
.services .divider{position:absolute;top:128px;width:100%}
.service{position:absolute;width:508px;height:205px;background:#fff;display:flex;padding:14px;gap:14px;text-align:left}
.service .photo{flex:0 0 214px;height:177px}
.service h3{font-family:"Montserrat",sans-serif;font-size:13px;font-weight:700;text-transform:uppercase;line-height:18px;margin-top:2px}
.service p{font-size:11.5px;line-height:17px;color:var(--muted);margin-top:8px}
.more{color:var(--green);font-size:12px}

/* why */
.why{top:2569px;height:603px;background:#fff}
.why .heading{position:absolute;left:80px;top:66px;z-index:1}
.why .plants{position:absolute;left:0;top:120px;width:500px;height:466px;background:linear-gradient(180deg,#eef1ea 0%,#7fa35a 50%,#b7b2a6 100%)}
.why .divider{position:absolute;left:560px;top:72px}
.why .intro{position:absolute;left:524px;top:118px;width:596px;font-size:14px;line-height:24px;color:var(--muted)}
.checks{position:absolute;left:524px;top:236px;list-style:none}
.checks li{display:flex;align-items:center;gap:12px;height:33px;font-size:13px;color:var(--green)}
.btn{display:inline-block;background:var(--orange);color:#fff;font-family:"Montserrat",sans-serif;font-weight:700;font-size:12px;text-transform:uppercase;letter-spacing:.5px}
.why .btn{position:absolute;left:524px;top:527px;width:130px;height:34px;line-height:34px;text-align:center}

/* testimonial */
.testimonial{top:3172px;height:483px;background:var(--light)}
.testimonial .heading{position:absolute;top:94px;width:100%}
.testimonial .divider{position:absolute;top:152px;width:100%}
.portrait{position:absolute;left:192px;top:243px;width:176px;height:176px;border-radius:50%;background:radial-gradient(circle at 50% 40%,#d8cfc4,#8b8680);border:5px solid #fff}
.quote-text{position:absolute;left:407px;top:246px;width:600px;font-size:14px;line-height:24px;color:var(--muted);text-align:left}
.client{position:absolute;left:407px;top:354px;text-align:left}
.client b{display:block;color:var(--green);font-family:"Montserrat",sans-serif;font-size:13px;font-weight:600}
.client span{display:block;font-size:12px;color:var(--muted);margin-top:8px}
.arrow{position:absolute;top:312px}

/* blog */
.blog{top:3655px;height:621px;background:#fff}
.blog .heading{position:absolute;top:70px;width:100%}
.blog .divider{position:absolute;top:124px;width:100%}
.post{position:absolute;top:207px;width:328px;text-align:left}
.post .photo{height:207px;position:relative}
.date{position:absolute;left:0;top:0;width:52px;height:68px;background:var(--yellow);text-align:center;font-family:"Montserrat",sans-serif;color:var(--ink)}
.date b{display:block;font-size:22px;padding-top:10px}
.date span{display:block;font-size:10px;font-weight:700}
.post h3{margin-top:20px;font-family:"Montserrat",sans-serif;font-size:14px;font-weight:600;text-transform:uppercase}
.post p{margin-top:10px;font-size:12px;line-height:19px;color:var(--muted)}
.post .more{display:block;margin-top:12px;color:var(--red);font-size:12px}

/* quote */
.quote{top:4276px;height:672px;background:linear-gradient(100deg,#6a8f2f 0%,#c9c07a 30%,#e9d9a2 50%,#b7b472 70%,#e0a928 100%)}
.quote-panel{position:absolute;left:310px;top:75px;width:580px;height:597px;background:rgba(28,28,26,.93);padding:0 49px}
.quote-panel .heading{margin-top:80px;color:#fff;font-weight:700;font-size:26px;text-align:center}
.quote-panel .divider{margin-top:18px;justify-content:center}
.fields{margin-top:58px;display:grid;grid-template-columns:227px 227px;gap:21px 28px}
.field{height:48px;border:1px solid #777;color:#ddd;font-size:12px;padding:0 12px;display:flex;align-items:center;justify-content:space-between}
.field.wide{grid-column:1/3;height:93px;align-items:flex-start;padding-top:14px}
.quote-foot{margin-top:21px;display:flex;align-items:center;justify-content:space-between}
.quote-foot .btn{width:165px;height:41px;line-height:41px;text-align:center}
.call{color:#fff;font-size:13px}
.call b{color:var(--yellow);font-size:22px;font-weight:400;margin-left:6px}

/* footer */
.footer{top:4948px;height:224px;background:var(--footer);color:#cfcfcf}
.footer .links{position:absolute;left:80px;top:114px;display:flex;gap:16px;font-size:11px;text-transform:uppercase}
.footer .copy{position:absolute;left:80px;top:146px;font-size:11px;color:#999}
.follow{position:absolute;left:655px;top:90px;font-size:12px}
.footer .social{left:655px;top:136px}
.footer .social i{background:#fff;width:24px;height:24px}
.footer .logo{right:80px;top:120px;color:#fff;font-size:22px}
</style>
</head>
<body>

<header class="section topbar">
  <div class="contact">
    <span><svg width="12" height="12" viewBox="0 0 24 24"><path d="M6.6 10.8a15 15 0 0 0 6.6 6.6l2.2-2.2a1 1 0 0 1 1-.25 11.4 11.4 0 0 0 3.6.57 1 1 0 0 1 1 1V20a1 1 0 0 1-1 1A17 17 0 0 1 3 4a1 1 0 0 1 1-1h3.5a1 1 0 0 1 1 1c0 1.25.2 2.45.57 3.57a1 1 0 0 1-.25 1z" fill="#5c9a1b"/></svg>204-571-3342</span>
    <span><svg width="13" height="10" viewBox="0 0 26 20"><rect x="1" y="1" width="24" height="18" fill="none" stroke="#5c9a1b" stroke-width="2"/><path d="M1 1l12 10L25 1" fill="none" stroke="#5c9a1b" stroke-width="2"/></svg>ger.ostrunek@maplethorn.com</span>
  </div>
  <div class="estimate-tab">FREE ESTIMATES</div>
  <div class="social"><i></i><i></i><i></i><i></i></div>
</header>

<nav class="section nav">
  <div class="logo">COBALT<i></i>LANDSCAPING</div>
  <div class="menu"><span>HOME</span><span>ABOUT</span><span>SERVICES</span><span>WHY CHOOSE US</span><span>TESTIMONIALS</span><span>BLOG</span><span>CONTACTS</span></div>
</nav>

<section class="section hero" role="img" aria-label="Sunlit garden with a large tree, flowering shrubs and a white house">
  <div class="slogan one"><span>DEPENDABLE, RELIABLE</span></div>
  <div class="slogan two"><span>CONSISTENT</span></div>
</section>

<section class="section about center">
  <h2 class="heading"><b>ABOUT</b> COBALTLANDSCAPING</h2>
  <div class="divider"><span></span><i></i><span></span></div>
  <p class="lead">Lorem ipsum dolor sit amet, consectetur adipiscing elit. Nullam vehicula nunc ac imperdiet porta. Donec vel elit mi. Donec lectus libero, bibendum quis ex in, tincidunt imperdiet orci.</p>
  <div class="features">
    <div class="feature f-purple"><div class="badge"><svg width="20" height="22" viewBox="0 0 20 22"><path d="M10 1l8 3v6c0 5-3.5 9-8 11-4.5-2-8-6-8-11V4z" fill="#fff"/></svg></div><div class="label">5 Years of Experience</div></div>
    <div class="feature f-red"><div class="badge"><svg width="22" height="20" viewBox="0 0 22 20"><path d="M2 9h4v10H2zM8 19V9l4-8c1.6 0 2.5 1 2.2 2.6L13.5 7H19a2 2 0 0 1 2 2.3l-1.3 7.5A2.5 2.5 0 0 1 17.2 19z" fill="#fff"/></svg></div><div class="label">Honest &amp; Reliable</div></div>
    <div class="feature f-yellow"><div class="badge"><svg width="22" height="22" viewBox="0 0 24 24"><path d="M12 2l3 6.5 7 .8-5.2 4.8 1.5 7L12 17.6 5.7 21.1l1.5-7L2 9.3l7-.8z" fill="#fff"/></svg></div><div class="label">Great Service</div></div>
    <div class="feature f-blue"><div class="badge"><svg width="22" height="22" viewBox="0 0 24 24"><circle cx="12" cy="12" r="9" fill="none" stroke="#fff" stroke-width="2.4"/><path d="M12 7v5l3 2" fill="none" stroke="#fff" stroke-width="2.4"/></svg></div><div class="label">24 Hour Free Helpline</div></div>
  </div>
</section>

<section class="section services center" role="img" aria-label="Dark garden backdrop with watering can and foliage">
  <h2 class="heading"><b>OUR</b> SERVICES</h2>
  <div class="divider"><span></span><i></i><span></span></div>

  <article class="service" style="left:80px;top:217px">
    <div class="photo" role="img" aria-label="Orange and yellow perennial flowers" style="background:linear-gradient(135deg,#e8a21f,#c8501a 55%,#4c6e1e)"></div>
    <div><h3>Weeding of Perennial &amp; Flower Beds</h3><p>Donec ac felis fermentum, faucibus tortor sit amet, elementum risus. Nam pretium justo neque, id imperdiet tortor rhoncus interdum. Morbi faucibus ex id semper dictum. Ut tincidunt integer cursus vitae ligula et faucibus.</p><span class="more">Read More...</span></div>
  </article>
  <article class="service" style="left:612px;top:217px">
    <div class="photo" role="img" aria-label="Pruned shrubs with pink blossoms" style="background:linear-gradient(135deg,#d9c7b6,#b0445f 50%,#5a6b2c)"></div>
    <div><h3>Selective Pruning of Trees &amp; Shrubs</h3><p>Donec ac felis fermentum, faucibus tortor sit amet, elementum risus. Nam pretium justo neque, id imperdiet tortor rhoncus interdum. Morbi faucibus ex id semper dictum. Ut tincidunt integer cursus vitae ligula et faucibus.</p><span class="more">Read More...</span></div>
  </article>
  <article class="service" style="left:80px;top:448px">
    <div class="photo" role="img" aria-label="Neatly clipped round hedges" style="background:linear-gradient(160deg,#9dbd5c,#3d6b1a 60%,#2a4a12)"></div>
    <div><h3>Hedging</h3><p>Donec ac felis fermentum, faucibus tortor sit amet, elementum risus. Nam pretium justo neque, id imperdiet tortor rhoncus interdum. Morbi faucibus ex id semper dictum. Ut tincidunt integer cursus vitae ligula et faucibus.</p><span class="more">Read More...</span></div>
  </article>
  <article class="service" style="left:612px;top:448px">
    <div class="photo" role="img" aria-label="Stone patio with modern outdoor seating" style="background:linear-gradient(160deg,#dfe6ea,#b9b8ac 55%,#6f7d55)"></div>
    <div><h3>Landscape Construction</h3><p>Donec ac felis fermentum, faucibus tortor sit amet, elementum risus. Nam pretium justo neque, id imperdiet tortor rhoncus interdum. Morbi faucibus ex id semper dictum. Ut tincidunt integer cursus vitae ligula et faucibus.</p><span class="more">Read More...</span></div>
  </article>
  <article class="service" style="left:80px;top:679px">
    <div class="photo" role="img" aria-label="Designed garden beds with colourful flowers" style="background:linear-gradient(170deg,#6f9a3a,#c33a7a 55%,#e2b52a)"></div>
    <div><h3>Landscape Design</h3><p>Donec ac felis fermentum, faucibus tortor sit amet, elementum risus. Nam pretium justo neque, id imperdiet tortor rhoncus interdum. Morbi faucibus ex id semper dictum. Ut tincidunt integer cursus vitae ligula et faucibus.</p><span class="more">Read More...</span></div>
  </article>
  <article class="service" style="left:612px;top:679px">
    <div class="photo" role="img" aria-label="Dense green garden foliage" style="background:linear-gradient(160deg,#8ab04a,#4a7420 55%,#2f4f16)"></div>
    <div><h3>Total Lawn Treatment Plans</h3><p>Donec ac felis fermentum, faucibus tortor sit amet, elementum risus. Nam pretium justo neque, id imperdiet tortor rhoncus interdum. Morbi faucibus ex id semper dictum. Ut tincidunt integer cursus vitae ligula et faucibus.</p><span class="more">Read More...</span></div>
  </article>
  <article class="service" style="left:348px;top:910px">
    <div class="photo" role="img" aria-label="Red flowering plant leaves" style="background:linear-gradient(150deg,#3f6a1c,#c8242c 55%,#5d7f2a)"></div>
    <div><h3>Landscape Pest Control</h3><p>Donec ac felis fermentum, faucibus tortor sit amet, elementum risus. Nam pretium justo neque, id imperdiet tortor rhoncus interdum. Morbi faucibus ex id semper dictum. Ut tincidunt integer cursus vitae ligula et faucibus.</p><span class="more">Read More...</span></div>
  </article>
</section>

<section class="section why">
  <div class="plants" role="img" aria-label="Potted green plants on a wooden table"></div>
  <h2 class="heading"><b>WHY</b> CHOOSE US</h2>
  <div class="divider"><span></span><i></i><span></span></div>
  <p class="intro">Lorem ipsum dolor sit amet, consectetur adipiscing elit. Nullam vehicula nunc ac imperdiet porta. Donec vel elit mi. Donec lectus libero, bibendum quis ex in, tincidunt imperdiet orci.</p>
  <ul class="checks">
    <li><svg width="14" height="12" viewBox="0 0 14 12"><path d="M1 6l4 4 8-9" fill="none" stroke="#d7262b" stroke-width="2.4"/></svg>Lorem ipsum dolor sit amet, consectetur adipiscing elit.</li>
    <li><svg width="14" height="12" viewBox="0 0 14 12"><path d="M1 6l4 4 8-9" fill="none" stroke="#d7262b" stroke-width="2.4"/></svg>Proin eu velit a odio volutpat porta in nec libero.</li>
    <li><svg width="14" height="12" viewBox="0 0 14 12"><path d="M1 6l4 4 8-9" fill="none" stroke="#d7262b" stroke-width="2.4"/></svg>Nam convallis sem id justo eleifend ultrices.</li>
    <li><svg width="14" height="12" viewBox="0 0 14 12"><path d="M1 6l4 4 8-9" fill="none" stroke="#d7262b" stroke-width="2.4"/></svg>Donec est lacus finibus, facilisis leo sed, scelerisque lacus.</li>
    <li><svg width="14" height="12" viewBox="0 0 14 12"><path d="M1 6l4 4 8-9" fill="none" stroke="#d7262b" stroke-width="2.4"/></svg>Sed et velit eu tortor egestas venenatis.</li>
    <li><svg width="14" height="12" viewBox="0 0 14 12"><path d="M1 6l4 4 8-9" fill="none" stroke="#d7262b" stroke-width="2.4"/></svg>Sed lobortis nisi a velit fringilla ullamcorper.</li>
    <li><svg width="14" height="12" viewBox="0 0 14 12"><path d="M1 6l4 4 8-9" fill="none" stroke="#d7262b" stroke-width="2.4"/></svg>Phasellus rhoncus ex id cursus varius.</li>
  </ul>
  <span class="btn">Contact Us</span>
</section>

<section class="section testimonial center">
  <h2 class="heading"><b>CLIENTS'</b> TESTIMONIAL</h2>
  <div class="divider"><span></span><i></i><span></span></div>
  <svg class="arrow" style="left:144px" width="12" height="20" viewBox="0 0 12 20"><path d="M10 2L2 10l8 8" fill="none" stroke="#777" stroke-width="2"/></svg>
  <div class="portrait" role="img" aria-label="Client portrait"></div>
  <p class="quote-text">Curabitur ac urna varius ante dapibus tempus lobortis quis turpis. Nam ut metus dolor. Nunc ipsum metus, sodales eget pharetra nec, interdum quis ex. Morbi efficitur orci.</p>
  <div class="client"><b>HARLAN MERCER</b><span>Chief Secretary, Vellmont Group</span></div>
  <svg class="arrow" style="left:1044px" width="12" height="20" viewBox="0 0 12 20"><path d="M2 2l8 8-8 8" fill="none" stroke="#777" stroke-width="2"/></svg>
</section>

<section class="section blog center">
  <h2 class="heading"><b>LATEST</b> BLOG</h2>
  <div class="divider"><span></span><i></i><span></span></div>
  <article class="post" style="left:80px">
    <div class="photo" role="img" aria-label="Large house with landscaped front garden" style="background:linear-gradient(180deg,#cfe0ef,#b8a58a 45%,#5e8a2c)"><div class="date"><b>29</b><span>APRIL</span></div></div>
    <h3>Proin diam purus, posuere nec elit.</h3>
    <p>Nulla ac neque pharetra, elementum enim in, finibus erat. Curabitur in odio in risus fermentum cursus. Morbi nec ultrices orci.</p>
    <span class="more">READ MORE&gt;&gt;</span>
  </article>
  <article class="post" style="left:434px">
    <div class="photo" role="img" aria-label="Formal garden with flower borders" style="background:linear-gradient(180deg,#7fa03e,#c75a8a 55%,#4b7a22)"><div class="date"><b>29</b><span>APRIL</span></div></div>
    <h3>Proin diam purus, posuere nec elit.</h3>
    <p>Nulla ac neque pharetra, elementum enim in, finibus erat. Curabitur in odio in risus fermentum cursus. Morbi nec ultrices orci.</p>
    <span class="more">READ MORE&gt;&gt;</span>
  </article>
  <article class="post" style="left:790px">
    <div class="photo" role="img" aria-label="Gardener tending flower beds" style="background:linear-gradient(180deg,#a8c460,#e07a2a 50%,#3f6a1a)"><div class="date"><b>29</b><span>APRIL</span></div></div>
    <h3>Proin diam purus, posuere nec elit.</h3>
    <p>Nulla ac neque pharetra, elementum enim in, finibus erat. Curabitur in odio in risus fermentum cursus. Morbi nec ultrices orci.</p>
    <span class="more">READ MORE&gt;&gt;</span>
  </article>
</section>

<section class="section quote" role="img" aria-label="Sunlit flower bed with yellow rubber boots and garden tools">
  <div class="quote-panel">
    <h2 class="heading">GET AN INSTANT QUOTE</h2>
    <div class="divider"><span></span><i></i><span></span></div>
    <div class="fields">
      <div class="field">Full Name</div>
      <div class="field">Phone Number</div>
      <div class="field">Email ID</div>
      <div class="field">Service Required <svg width="10" height="6" viewBox="0 0 10 6"><path d="M1 1l4 4 4-4" fill="none" stroke="#ddd" stroke-width="1.5"/></svg></div>
      <div class="field wide">How Can We Help</div>
    </div>
    <div class="quote-foot">
      <span class="btn">Get Free Estimate</span>
      <span class="call">Or Call Us:<b>(204-571-3342)</b></span>
    </div>
  </div>
</section>

<footer class="section footer">
  <div class="links"><span>Home</span><span>About</span><span>Services</span><span>Why Choose Us</span><span>Testimonials</span><span>Blog</span><span>Contacts</span></div>
  <div class="copy">© cobaltlandscaping.com. All Rights Reserved</div>
  <div class="follow">Follow Us</div>
  <div class="social"><i></i><i></i><i></i></div>
  <div class="logo">COBALT<i></i>LANDSCAPING</div>
</footer>

</body>
</html>
```